Calvanta Group Real Estate Company business cards

New business card design, we are generally happy with the basic layout of the existing front of business card, (feel free to change) but require a head shot photo on the back side.

http://www.calvanta.com.au/

Attached logos, and existing business card

------------------------------

Target Market(s)

Real estate

Industry/Entity Type

Real Estate

Contact Information for Business Card

Standard size double sided

Font styles to use
Other font styles liked:
• Futura

Requirements
Must have
• Photo head shot on the back side
Nice to have
• yes
Should not have
• No

```html
<!DOCTYPE html>
<html lang="en">
<head>
<meta charset="utf-8">
<title>Calvanta Group – Business Cards</title>
<link rel="stylesheet" href="https://fonts.googleapis.com/css2?family=Jost:wght@400;600&display=swap">
<style>
  :root {
    --purple: #3d2b6b;
    --purple-deep: #2f2156;
    --orange: #f5a01a;
    --white: #ffffff;
    --paper: #f3f3f4;
    --backdrop: #d4d4d6;
    --ink-soft: #e9e6f2;
  }
  * { box-sizing: border-box; margin: 0; padding: 0; }
  html, body {
    width: 1200px; height: 914px; overflow: hidden;
    background: var(--backdrop);
    font-family: "Jost", "Futura", sans-serif;
  }
  .sheet {
    width: 1200px; height: 914px;
    display: flex; flex-direction: column; align-items: center; justify-content: center;
    gap: 56px;
  }
  .card {
    position: relative;
    width: 620px; height: 379px;
    border-radius: 4px;
    overflow: hidden;
    box-shadow: 0 6px 18px rgba(0,0,0,.18);
  }
  /* Front side */
  .card--front {
    background: var(--paper);
    display: flex; flex-direction: column; align-items: center; justify-content: center;
    gap: 22px;
  }
  .brand-name {
    font-weight: 400;
    letter-spacing: 1px;
    line-height: 1;
  }
  .card--front .brand-name { color: var(--purple); font-size: 64px; }
  .tagline {
    color: var(--purple);
    font-weight: 600;
    font-size: 19px;
    letter-spacing: 3px;
  }
  /* Back side */
  .card--back { background: var(--purple); color: var(--white); }
  .card--back .brand-name {
    position: absolute; left: 38px; top: 62px;
    color: var(--white); font-size: 50px;
  }
  .role-line {
    position: absolute; left: 40px; top: 168px;
    font-size: 20px; white-space: nowrap;
  }
  .person-name { color: var(--orange); font-weight: 600; letter-spacing: .5px; }
  .divider { margin: 0 12px; }
  .person-title { font-weight: 400; }
  .contact-list {
    position: absolute; left: 40px; top: 214px;
    list-style: none;
    display: flex; flex-direction: column; gap: 5px;
    font-size: 15px;
  }
  .contact-item { display: flex; align-items: center; gap: 9px; }
  .contact-icon {
    width: 18px; height: 18px; border-radius: 3px;
    background: var(--orange);
    display: flex; align-items: center; justify-content: center;
    flex: none;
  }
  .company-block {
    position: absolute; left: 40px; top: 306px;
    font-size: 14px; line-height: 1.35; letter-spacing: .3px;
  }
  .headshot {
    position: absolute; right: 0; top: 34px;
    width: 230px; height: 345px;
    background: linear-gradient(180deg, #5a4a86 0%, #3a4470 45%, #24305a 100%);
  }
</style>
</head>
<body>
<main class="sheet">
  <section class="card card--front" aria-label="Business card front">
    <div class="brand-name">Calvanta Group</div>
    <div class="tagline">BUY | SELL | RENT</div>
  </section>

  <section class="card card--back" aria-label="Business card back">
    <div class="brand-name">Calvanta Group</div>
    <div class="role-line">
      <span class="person-name">DANIEL TRAN</span><span class="divider">|</span><span class="person-title">Director</span>
    </div>
    <ul class="contact-list">
      <li class="contact-item">
        <span class="contact-icon">
          <svg width="12" height="12" viewBox="0 0 12 12"><rect x="3" y="1" width="6" height="10" rx="1" fill="none" stroke="#3d2b6b" stroke-width="1.4"/><circle cx="6" cy="9" r=".8" fill="#3d2b6b"/></svg>
        </span>0412 558 306
      </li>
      <li class="contact-item">
        <span class="contact-icon">
          <svg width="12" height="12" viewBox="0 0 12 12"><rect x="1.5" y="3" width="9" height="6.5" fill="none" stroke="#3d2b6b" stroke-width="1.3"/><path d="M1.5 3 L6 7 L10.5 3" fill="none" stroke="#3d2b6b" stroke-width="1.3"/></svg>
        </span>daniel.tran@calvanta.com.au
      </li>
      <li class="contact-item">
        <span class="contact-icon">
          <svg width="12" height="12" viewBox="0 0 12 12"><circle cx="6" cy="6" r="4.5" fill="none" stroke="#3d2b6b" stroke-width="1.2"/><ellipse cx="6" cy="6" rx="2" ry="4.5" fill="none" stroke="#3d2b6b" stroke-width="1"/><path d="M1.5 6 H10.5" stroke="#3d2b6b" stroke-width="1"/></svg>
        </span>www.calvanta.com.au
      </li>
    </ul>
    <div class="company-block">
      <div>CALVANTA GROUP</div>
      <div>ABN: 41 208 663 915</div>
    </div>
    <div class="headshot" role="img" aria-label="Head shot photo of the director in a navy suit and blue tie"></div>
  </section>
</main>
</body>
</html>
```